Banner Ad Design for Velvet Bridal Shop

Are you a Stylish Designer? Can you work with a balanced color wheel? Let your creative juices flow this way!

```html
<!DOCTYPE html>
<html lang="en">
<head>
<meta charset="UTF-8">
<title>Velvet Bridal Shop – Bridal Lingerie Banner</title>
<link href="https://fonts.googleapis.com/css2?family=Cormorant+SC:wght@500&family=Great+Vibes&display=swap" rel="stylesheet">
<style>
  :root {
    --blush: #f6d3cd;
    --blush-light: #fbe4df;
    --mauve: #a9636c;
    --mauve-deep: #95525c;
    --mauve-soft: #c98d93;
    --white: #ffffff;
  }
  html, body {
    margin: 0;
    padding: 0;
    overflow: hidden;
    background: var(--white);
  }
  .banner {
    position: relative;
    width: 1200px;
    height: 290px;
    overflow: hidden;
    background: var(--blush);
  }
  .banner__swoosh {
    position: absolute;
    inset: 0;
    width: 1200px;
    height: 290px;
  }
  .banner__ornament {
    position: absolute;
    left: 20px;
    top: 10px;
    width: 210px;
    height: 270px;
    border-radius: 50% 40% 50% 40%;
    background: radial-gradient(ellipse at 40% 60%, var(--mauve-soft) 0%, rgba(201,141,147,0) 70%);
  }
  .banner__product {
    position: absolute;
    left: 980px;
    top: 0;
    width: 200px;
    height: 290px;
    background: linear-gradient(180deg, var(--blush-light) 0%, #e9b3b0 45%, #d99ea0 100%);
    border-radius: 40% 40% 20% 20% / 12% 12% 8% 8%;
  }
  .banner__title {
    position: absolute;
    left: 372px;
    top: 18px;
    margin: 0;
    font-family: "Cormorant SC", "Times New Roman", serif;
    font-weight: 500;
    font-size: 70px;
    line-height: 1;
    letter-spacing: 1px;
    color: var(--white);
    white-space: nowrap;
  }
  .banner__tagline {
    position: absolute;
    left: 326px;
    top: 100px;
    margin: 0;
    font-family: "Great Vibes", cursive;
    font-weight: 400;
    font-size: 80px;
    line-height: 1;
    color: var(--mauve);
    white-space: nowrap;
  }
  .banner__cta {
    position: absolute;
    left: 612px;
    top: 212px;
    width: 318px;
    height: 52px;
    border-radius: 26px;
    background: var(--mauve);
    box-shadow: 0 0 0 2px var(--blush-light);
    color: var(--white);
    font-family: "Great Vibes", cursive;
    font-size: 40px;
    line-height: 52px;
    text-align: center;
    text-decoration: none;
  }
</style>
</head>
<body>
  <div class="banner">
    <svg class="banner__swoosh" viewBox="0 0 1200 290" aria-hidden="true">
      <path d="M0 0 H300 C190 80 230 215 610 290 H0 Z" fill="var(--mauve)"/>
      <path d="M0 170 C120 230 260 260 420 290 H0 Z" fill="var(--mauve-deep)" opacity="0.5"/>
    </svg>
    <div class="banner__ornament" role="img" aria-label="Delicate floral flourish with a calla lily"></div>
    <div class="banner__product" role="img" aria-label="Pink bridal corset with garter straps"></div>
    <h1 class="banner__title">Bridal Lingerie</h1>
    <p class="banner__tagline">Gorgeous, sweet &amp; petite!</p>
    <a class="banner__cta" href="#catalogue">view catalogue</a>
  </div>
</body>
</html>
```